Real Estate Open House & For Sale Signage

I am designing brand new signs for my real estate company. All I have so far are my logo and a business card design. I would like to have designed two different signs, 1. Open House directional sign, 2. For Sale Company sign. Both signs need to will be eye catching from the street, easy to read, identifiable and memorable.

Target Market(s)

Males & females, Ages between 30-65, affluent, educated, professionals.

Industry/Entity Type

Real Estate

Font styles to use
Serif
Sans Serif

Colors
33b8a4
34a7d8
acd137
3277b5

Requirements
Must have
• Must have my company logo & real estate license number visible on the sign. Must be easily visible and eye catching from a moving vehicle. Must have a professional and trustworthy appeal. Must bring to mind real estate.
Nice to have
• Image or icon that will denote real estate and be known as a part of my company identity and marketing theme.
Should not have
• Attached is a feeble attempt at creating my For Sale sign. The information on the sign is accurate, but the design is not appealing to me at all. It feels very amateurish.

```html
<!DOCTYPE html>
<html lang="en">
<head>
<meta charset="utf-8">
<title>For Sale Sign</title>
<link href="https://fonts.googleapis.com/css2?family=Libre+Baskerville:wght@700&family=Oswald:wght@500;600&display=swap" rel="stylesheet">
<style>
  :root {
    --brand-green: #afd137;
    --ink: #1d1d1d;
    --sign-white: #ffffff;
    --backdrop: #e9ecef;
  }
  html, body {
    margin: 0;
    padding: 0;
    width: 1200px;
    height: 930px;
    overflow: hidden;
    background: var(--backdrop);
  }
  .sign {
    position: absolute;
    left: 320px;
    top: 35px;
    width: 560px;
    height: 860px;
    background: var(--sign-white);
    overflow: hidden;
    box-shadow: 0 2px 10px rgba(0,0,0,0.12);
  }
  .sign__header {
    position: absolute;
    left: 0; top: 0;
    width: 100%;
    height: 290px;
    background: var(--brand-green);
  }
  .sign__headline {
    position: absolute;
    left: 0;
    top: 62px;
    width: 100%;
    margin: 0;
    text-align: center;
    font-family: "Libre Baskerville", serif;
    font-weight: 700;
    font-size: 80px;
    line-height: 1.1;
    letter-spacing: 1px;
    color: var(--sign-white);
  }
  .license {
    position: absolute;
    right: 80px;
    top: 312px;
    font-family: "Oswald", sans-serif;
    font-weight: 500;
    font-size: 16px;
    color: var(--ink);
  }
  .company {
    position: absolute;
    left: 0;
    top: 345px;
    width: 100%;
    display: flex;
    align-items: center;
    justify-content: center;
    gap: 22px;
  }
  .company__dot {
    flex: none;
    width: 44px;
    height: 44px;
    border-radius: 50%;
    background: var(--brand-green);
  }
  .company__name {
    font-family: "Oswald", sans-serif;
    font-weight: 500;
    font-size: 62px;
    line-height: 68px;
    letter-spacing: 4px;
    color: var(--brand-green);
    text-transform: uppercase;
  }
  .tagline {
    position: absolute;
    left: 45px;
    top: 560px;
    width: 470px;
    height: 54px;
    border-radius: 8px;
    background: var(--ink);
    color: var(--sign-white);
    font-family: "Oswald", sans-serif;
    font-weight: 500;
    font-size: 29px;
    line-height: 54px;
    text-align: center;
  }
  .agent {
    position: absolute;
    left: 0;
    top: 640px;
    width: 100%;
    text-align: center;
    font-family: "Oswald", sans-serif;
    font-weight: 500;
    font-size: 28px;
    line-height: 40px;
    color: var(--ink);
  }
  .phone {
    position: absolute;
    left: 0;
    top: 680px;
    width: 100%;
    text-align: center;
    font-family: "Oswald", sans-serif;
    font-weight: 600;
    font-size: 84px;
    line-height: 120px;
    color: var(--brand-green);
  }
</style>
</head>
<body>
  <main class="sign">
    <header class="sign__header">
      <h1 class="sign__headline">FOR SALE</h1>
    </header>
    <div class="license">RB-40512</div>
    <div class="company">
      <span class="company__dot"></span>
      <span class="company__name">Maple Harbor<br>Realty LLC</span>
    </div>
    <div class="tagline">YOUR NEIGHBORHOOD SPECIALIST</div>
    <div class="agent">LENA PARK, RB- 31274</div>
    <div class="phone">(808) 555-0143</div>
  </main>
</body>
</html>
```